Free Charity Events from KORVAPLAY

The purpose of the landing page is to get all visitors excited about playing in our Free $500 Charity Tournaments. The visitors who click on the landing page will receive 3 free entries into 3 different $500 Charity Tournaments. A $500 Blackjack Tournament, a $500 Texas Holdem Tournament, and a $500 Baccarat Tournament.

We also offer Free Qualifying games 24/7, where players can earn additional entries into our real paying tournaments.

We will reward the winners in each tournament with a share of the $500 and we will reward a worthy cause or charity with $500 as well.

The money comes from advertising shown during the qualifying game.

Our website is currently being developed on our teams development server. Here is a private link to the site. https://dev.korvaplay.example Attached are vector images of our logo.

Also attached are two attempts we made at a landing page.

Target Market(s)

Social Game Players

Industry/Entity Type

Games

Contact Information for Business Card

The purpose of the business card will be to promote our Free Charity Games. There will be a code hand written on the card. (Meaning we will need a white box to write the code in) If the holder of the card enters that code during registration, they will receive 3 free entries into our real cash tournaments. The giver of the card will receive the affiliate bonus for referring a new player.

Font styles to use
Serif
Sans Serif

Colors
9bcb3c
0292cd
ec1f27

Requirements
Must have
• Excitement, i also like humor but that isn't a must, excitement is.
Nice to have
• Humor
Should not have
• Too many words, we are looking for that image that says at least a few hundred words.

```html
<!DOCTYPE html>
<html lang="en">
<head>
<meta charset="utf-8">
<title>KORVAPLAY – Free Charity Tournaments</title>
<link rel="stylesheet" href="https://fonts.googleapis.com/css2?family=Noto+Sans:ital,wght@0,400;0,700;0,800;0,900;1,800;1,900&family=Open+Sans:wght@400;600;700&display=swap">
<style>
  :root {
    --sky: #cfdeeb;
    --sky-deep: #b9cbdc;
    --white: #ffffff;
    --red: #d0021b;
    --blue: #2f74b0;
    --blue-dark: #2a5a9a;
    --green: #8ab440;
    --button: #a9c77a;
    --field-border: #b5cde0;
  }
  * { box-sizing: border-box; margin: 0; padding: 0; }
  html, body { width: 1200px; height: 878px; overflow: hidden; background: var(--sky); }
  .landing {
    position: relative;
    width: 1200px;
    height: 878px;
    background: var(--sky);
    font-family: "Open Sans", sans-serif;
  }
  .hero-photo {
    position: absolute;
    left: 0; top: 0;
    width: 666px; height: 878px;
    background:
      radial-gradient(ellipse at 30% 45%, #e6c9b8 0%, rgba(230,201,184,0) 38%),
      radial-gradient(ellipse at 20% 30%, #8a6a52 0%, rgba(138,106,82,0) 45%),
      linear-gradient(120deg, #dfe8f0 0%, #c9d7e4 55%, #d7e2ec 100%);
  }
  .panel {
    position: absolute;
    left: 666px; top: 0;
    width: 441px; height: 878px;
    background: var(--white);
    text-align: center;
  }
  .brand {
    position: absolute;
    left: 22px; top: 70px;
    width: 400px; height: 100px;
    display: flex; align-items: center; gap: 14px;
  }
  .brand-dot {
    width: 88px; height: 88px; border-radius: 50%;
    background: var(--green); flex: none;
  }
  .brand-name {
    font-family: "Noto Sans", sans-serif;
    font-weight: 800;
    font-size: 46px;
    color: var(--blue);
    letter-spacing: 0.5px;
  }
  .tagline {
    position: absolute; left: 0; right: 0; top: 180px;
    font-family: "Noto Sans", sans-serif; font-weight: 800;
    font-size: 30px; color: var(--red);
  }
  .headline {
    position: absolute; left: 0; right: 0; top: 228px;
    font-family: "Noto Sans", sans-serif; font-weight: 900;
    font-size: 62px; line-height: 1; color: var(--blue);
    letter-spacing: 2px;
    text-shadow: 2px 2px 2px rgba(0,0,0,0.25);
  }
  .subhead {
    position: absolute; left: 20px; right: 0; top: 292px;
    text-align: left;
    font-family: "Noto Sans", sans-serif; font-weight: 900; font-style: italic;
    font-size: 29px; line-height: 35px;
    text-shadow: 1px 1px 2px rgba(0,0,0,0.2);
  }
  .subhead .green { color: var(--green); }
  .subhead .red { color: var(--red); }
  .subhead .blue { color: var(--blue); }
  .games {
    position: absolute; left: 22px; right: 0; top: 382px;
    display: flex; gap: 6px; align-items: center;
    font-family: "Open Sans", sans-serif; font-weight: 600;
    font-size: 19px; color: var(--green);
  }
  .games li { list-style: none; display: flex; align-items: center; gap: 3px; }
  .games svg { width: 20px; height: 20px; }
  .offer {
    position: absolute; left: 0; right: 0; top: 428px;
    font-size: 19px; line-height: 25px; color: var(--blue);
    font-weight: 400;
  }
  .signup-field {
    position: absolute; left: 24px; top: 502px;
    width: 395px; height: 36px;
    border: 1px solid var(--field-border); border-radius: 18px;
    display: flex; align-items: center; justify-content: center;
    font-family: "Noto Sans", sans-serif; font-weight: 700;
    font-size: 23px; color: var(--red);
  }
  .signup-button {
    position: absolute; left: 115px; top: 558px;
    width: 216px; height: 36px;
    background: var(--button);
    display: flex; align-items: center; justify-content: center;
    font-family: "Noto Sans", sans-serif; font-weight: 700;
    font-size: 18px; color: var(--red); letter-spacing: 0.5px;
  }
  .share-title {
    position: absolute; left: 0; right: 0; top: 610px;
    font-family: "Noto Sans", sans-serif; font-weight: 700;
    font-size: 19px; color: var(--blue); letter-spacing: 0.5px;
  }
  .share-links {
    position: absolute; left: 126px; top: 648px;
    display: flex; gap: 8px;
  }
  .share-links span {
    width: 42px; height: 42px; border-radius: 50%; display: block;
  }
  .share-links .one { background: var(--blue-dark); }
  .share-links .two { background: #4f7fa6; }
  .share-links .three { background: var(--red); }
  .share-links .four { background: #5a9ad6; }
  .footer {
    position: absolute; left: 0; right: 0; top: 848px;
    font-size: 9px; color: var(--blue); font-weight: 600;
  }
</style>
</head>
<body>
<main class="landing">
  <div class="hero-photo" role="img" aria-label="Photo of a young woman cheering with a raised fist while looking at her phone"></div>

  <section class="panel">
    <div class="brand">
      <span class="brand-dot"></span>
      <span class="brand-name">KORVAPLAY</span>
    </div>

    <p class="tagline">Where Everyone Wins!</p>
    <h1 class="headline">PLAY FREE</h1>
    <p class="subhead">
      <span class="green">IN OUR THREE </span><span class="red">$500</span><br>
      <span class="blue">CHARITY TOURNAMENTS</span>
    </p>

    <ul class="games">
      <li><svg viewBox="0 0 24 24"><polygon points="12,2 15,9 22,9.5 16.5,14 18.5,21 12,17 5.5,21 7.5,14 2,9.5 9,9" fill="none" stroke="var(--red)" stroke-width="2"/></svg>BLACKJACK</li>
      <li><svg viewBox="0 0 24 24"><polygon points="12,2 15,9 22,9.5 16.5,14 18.5,21 12,17 5.5,21 7.5,14 2,9.5 9,9" fill="none" stroke="var(--red)" stroke-width="2"/></svg>HOLDEM</li>
      <li><svg viewBox="0 0 24 24"><polygon points="12,2 15,9 22,9.5 16.5,14 18.5,21 12,17 5.5,21 7.5,14 2,9.5 9,9" fill="none" stroke="var(--red)" stroke-width="2"/></svg>BACCARAT</li>
    </ul>

    <p class="offer">Subscribe email and get 3 free entries<br>into 3 different $500 Charity Tournaments</p>

    <div class="signup-field">Enter Your Email id here</div>
    <div class="signup-button">GET FREE ENTRIES</div>

    <p class="share-title">SHARE WITH US</p>
    <div class="share-links">
      <span class="one" role="img" aria-label="Share link"></span>
      <span class="two" role="img" aria-label="Share link"></span>
      <span class="three" role="img" aria-label="Share link"></span>
      <span class="four" role="img" aria-label="Share link"></span>
    </div>

    <p class="footer">© KORVAPLAY, ALL RIGHTS RESERVED 2019</p>
  </section>
</main>
</body>
</html>
```